Varbek - Nutritious Snacks and Desserts

We need a creative e-commerce website in which all features--buttons, background, etc.--convey our message: We sell delicious, nutritious snacks and desserts that most closely comply with the paleo diet guidelines. Our first product is Brunavo®--raw, vegan, paleo chocolate balls that are made of dates, coconut, and cocoa. Our products are organic, raw, irresistible and nutritious. We have several versions of Brunavo® in development, as well as mousse, ice cream, and crackers. Our mission is to purvey basic healthy foods. Our motto is, "Fuel for the Daily Trail-Seeker(tm)."

Target Market(s)

Health-conscious professionals who tend to shop at health food stores. Our products also meet the requirements of a gluten-free diet; and they also don't contain refined sugar, so shoppers with gluten and possibly sugar issues are incidental customers.

Industry/Entity Type

Health Product

Coding

Coded - Design and coding required

Number of Pages Required

5+ page

Colors

Designer to choose colors to be used in the design.

Requirements
Must have
• We need at least a home page, a products page, an about-us page, a contact page, and a shopping cart page. We would like to be able to add products on our own later. We should be able to handle some basic coding, especially if it's just a matter of copying and modifying product pages. We would also like the ability in the future to add blogging pages, allowing us to write articles about health food and healthy lifestyle, thus attracting web-traffic (SEO).
• Other features we would like to have:
• Product photo slider on the hopepage
• Back-to-top button at the bottom of the home page
• Make sure the site is mobile-compatible
• A search bar at the top of the homepage
• "Create an account" and "Previous orders"--allowing customers to see their previous orders and reorder what they purchased in the past.
Nice to have
• We would like to convey the paleo theme without actually stating it anywhere. We'll add text as necessary, according to the page layout; you can use ipsum lorem for purpose of demonstration.

```html
<!DOCTYPE html>
<html lang="en">
<head>
<meta charset="utf-8">
<title>Varbek – Nutritious Snacks and Desserts</title>
<link href="https://fonts.googleapis.com/css2?family=Raleway:wght@400;500;600;700;800&family=Open+Sans:wght@400;600;700&display=swap" rel="stylesheet">
<style>
:root{
  --green:#82c41e;
  --green-dark:#6faa14;
  --ink:#222;
  --text:#444;
  --muted:#777;
  --light:#f3f3f3;
  --line:#e2e2e2;
  --footer:#333333;
  --footer-line:#4a4a4a;
  --footer-text:#d6d6d6;
}
*{box-sizing:border-box;margin:0;padding:0}
html,body{width:718px;height:1200px;overflow:hidden;background:#fff}
body{position:relative;font-family:"Open Sans",sans-serif;color:var(--text)}
.abs{position:absolute}

/* header */
.topbar{left:0;top:0;width:718px;height:3px;background:var(--green)}
.brand{left:96px;top:14px;display:flex;align-items:center;gap:6px}
.brand-dot{width:30px;height:30px;border-radius:50%;background:var(--green)}
.brand-name{font-family:"Raleway",sans-serif;font-weight:700;font-size:21px;color:var(--green);letter-spacing:.5px}
.search{left:384px;top:18px;width:164px;height:22px;border:1px solid var(--line);display:flex}
.search-field{flex:1;font-size:6.5px;font-style:italic;color:var(--muted);padding:7px 6px}
.search-btn{width:28px;border-left:1px solid var(--line);display:flex;align-items:center;justify-content:center}
.basket{left:556px;top:17px;display:flex;gap:6px}
.basket-title{font-family:"Raleway",sans-serif;font-weight:700;font-size:11.5px;color:var(--green);line-height:13px}
.basket-count{font-size:6.5px;color:var(--ink)}
.nav{left:0;top:58px;width:718px;height:10px}
.nav a{position:absolute;font-family:"Raleway",sans-serif;font-weight:600;font-size:7.4px;color:var(--ink);text-decoration:none;letter-spacing:.2px}
.nav a.active{color:var(--green)}

/* hero */
.hero{left:0;top:78px;width:718px;height:296px;background:linear-gradient(100deg,#5a3a25 0%,#7a5037 30%,#b58a5c 55%,#e6d0a8 70%,#8a5a35 100%)}
.hero-photo{position:absolute;inset:0;background:radial-gradient(ellipse 130px 120px at 440px 130px,rgba(240,215,160,.85),rgba(200,140,70,.5) 60%,transparent 100%),linear-gradient(180deg,rgba(220,220,220,.55) 0%,transparent 35%)}
.hero-title{left:96px;top:165px;font-family:"Raleway",sans-serif;font-weight:800;font-size:24px;line-height:27px;color:#fff}
.hero-btn{left:96px;top:254px;width:98px;height:28px;border-radius:14px;background:var(--green);color:#fff;font-family:"Raleway",sans-serif;font-weight:600;font-size:8.5px;display:flex;align-items:center;justify-content:center}
.hero-arrow{top:204px;width:20px;height:20px;border:1px solid #fff;border-radius:50%;display:flex;align-items:center;justify-content:center}

/* welcome */
.welcome{left:0;top:374px;width:718px;height:135px;background:var(--light);text-align:center}
.section-title{font-family:"Raleway",sans-serif;font-weight:700;font-size:15.5px;color:var(--ink)}
.section-title span{color:var(--green)}
.welcome .section-title{margin-top:23px}
.welcome-text{margin:12px auto 0;width:400px;font-size:8.2px;line-height:13px;color:var(--ink)}
.welcome-tag{margin-top:9px;font-family:"Raleway",sans-serif;font-weight:500;font-size:12.5px;color:var(--ink)}

/* products */
.featured-title{left:0;top:531px;width:718px;text-align:center}
.card{top:569px;width:122px;height:185px;border:1px solid var(--line);text-align:center;background:#fff}
.card-photo{height:89px;margin:-1px -1px 0}
.card-price{margin-top:13px;font-family:"Raleway",sans-serif;font-weight:700;font-size:8.8px;color:var(--green)}
.card-desc{margin-top:6px;font-size:6.4px;line-height:10.5px;color:var(--text)}
.card-stars{margin-top:3px;font-size:6px;letter-spacing:.8px;color:#ccc}
.card-btn{margin:6px auto 0;width:64px;height:16px;border:1px solid #555;border-radius:8px;font-family:"Raleway",sans-serif;font-weight:700;font-size:5.8px;color:var(--ink);display:flex;align-items:center;justify-content:center}
.card-btn.primary{background:var(--green);border-color:var(--green);color:#fff}
.card-heart{position:absolute;right:9px;top:12px}

/* quote band */
.quote{left:0;top:777px;width:718px;height:122px;background:var(--green);text-align:center;color:#fff}
.quote-title{margin-top:27px;font-family:"Raleway",sans-serif;font-weight:500;font-size:20px}
.quote-text{margin:9px auto 0;width:400px;font-size:7.3px;line-height:11.2px;color:#eef7df}

/* newsletter */
.newsletter{left:0;top:899px;width:718px;height:105px;background:linear-gradient(180deg,#f7f7f5,#ececea);overflow:hidden}
.bowl{position:absolute;left:82px;top:20px;width:104px;height:104px;border-radius:50%;background:radial-gradient(circle at 50% 50%,#c8733a 0%,#b8863e 40%,#9a6a3c 75%,#d8b98f 100%)}
.news-title{position:absolute;left:0;top:14px;width:718px;text-align:center;font-family:"Raleway",sans-serif;font-weight:500;font-size:16px;color:var(--ink)}
.news-sub{position:absolute;left:0;top:38px;width:718px;text-align:center;font-size:7.5px;color:var(--text)}
.news-form{position:absolute;left:204px;top:59px;width:312px;height:24px;border:1px solid var(--line);border-radius:12px;background:#fff;overflow:hidden;display:flex}
.news-field{flex:1;font-size:6.2px;font-style:italic;color:var(--muted);padding:8px 9px}
.news-btn{width:47px;background:var(--green);color:#fff;font-family:"Raleway",sans-serif;font-weight:700;font-size:7px;display:flex;align-items:center;justify-content:center}

/* footer */
.footer{left:0;top:1004px;width:718px;height:196px;background:var(--footer)}
.foot-col{position:absolute;top:19px}
.foot-head{font-family:"Raleway",sans-serif;font-weight:500;font-size:10px;color:#fff}
.foot-list{list-style:none;margin-top:25px;font-size:6.4px;line-height:11.2px;color:var(--footer-text)}
.foot-rule{left:97px;top:1046px;width:525px;height:1px;background:var(--footer-line)}
.foot-accent{top:1045px;width:13px;height:2px;background:var(--green)}
.contact-row{display:flex;gap:7px;font-size:6.4px;line-height:11px;color:var(--footer-text);margin-bottom:4px}
.contact-icon{width:13px;height:13px;border:1px solid #888;border-radius:50%;flex:none;display:flex;align-items:center;justify-content:center}
.foot-bottom{left:97px;top:1161px;width:525px;height:1px;background:var(--footer-line)}
.social{top:1170px;width:16px;height:16px;border-radius:50%}
.copyright{left:400px;top:1176px;width:222px;text-align:right;font-size:6.2px;color:var(--footer-text)}
</style>
</head>
<body>

<div class="abs topbar"></div>

<header>
  <div class="abs brand">
    <div class="brand-dot"></div>
    <div class="brand-name">Varbek</div>
  </div>
  <div class="abs search">
    <div class="search-field">Enter keyword</div>
    <div class="search-btn">
      <svg width="9" height="9" viewBox="0 0 10 10"><circle cx="4" cy="4" r="3" fill="none" stroke="#222" stroke-width="1.4"/><line x1="6.2" y1="6.2" x2="9" y2="9" stroke="#222" stroke-width="1.5"/></svg>
    </div>
  </div>
  <div class="abs basket">
    <svg width="24" height="22" viewBox="0 0 24 22"><path d="M1 2h4l3 11h12l3-8H7" fill="none" stroke="#82c41e" stroke-width="2.4" stroke-linejoin="round"/><path d="M7 5h16l-3 8H9z" fill="#82c41e"/><circle cx="10" cy="18" r="2" fill="#82c41e"/><circle cx="19" cy="18" r="2" fill="#82c41e"/></svg>
    <div>
      <div class="basket-title">Basket</div>
      <div class="basket-count">(0.00 items)</div>
    </div>
  </div>
  <nav class="abs nav">
    <a class="active" style="left:256px">HOME</a>
    <a style="left:310px">ALL PRODUCTS</a>
    <a style="left:399px">OFFERS</a>
    <a style="left:460px">PALEO DIET</a>
    <a style="left:534px">BLOG</a>
    <a style="left:586px">CONTACT</a>
  </nav>
</header>

<section class="abs hero">
  <div class="hero-photo" role="img" aria-label="Ice cream scoops with caramel sauce in a waffle bowl on a wooden table"></div>
  <h1 class="abs hero-title" style="top:87px">Fuel<br>for the Daily<br>Trail-Seeker™</h1>
  <div class="abs hero-btn" style="top:176px">MORE PRODUCTS</div>
  <div class="abs hero-arrow" style="left:21px;top:126px"><svg width="6" height="8" viewBox="0 0 6 8"><path d="M4.5 1L1.5 4l3 3" fill="none" stroke="#fff" stroke-width="1"/></svg></div>
  <div class="abs hero-arrow" style="left:686px;top:126px"><svg width="6" height="8" viewBox="0 0 6 8"><path d="M1.5 1l3 3-3 3" fill="none" stroke="#fff" stroke-width="1"/></svg></div>
</section>

<section class="abs welcome">
  <h2 class="section-title">WELCOME TO <span>VARBEK FOODS.</span></h2>
  <p class="welcome-text">Our products are raw, organic, vegan, gluten-free, dairy-free, fiber-rich, nutrient-dense, antioxidant-rich real foods with no preservatives, no added sugar, and no artificial or plant-based sweeteners.</p>
  <p class="welcome-tag">And they are irresistibly scrumptious!</p>
</section>

<h2 class="abs section-title featured-title">FEATURED <span>PRODUCTS</span></h2>

<article class="abs card" style="left:97px">
  <div class="card-photo" role="img" aria-label="Banana pudding in a glass with mint" style="background:linear-gradient(180deg,#eeeeea,#f1e9b8 55%,#e6dc9a)"></div>
  <svg class="card-heart" width="8" height="7" viewBox="0 0 8 7"><path d="M4 6.5L1 3.5A1.6 1.6 0 0 1 4 1.5a1.6 1.6 0 0 1 3 2z" fill="none" stroke="#555" stroke-width=".8"/></svg>
  <div class="card-price">$ 150.00</div>
  <p class="card-desc">Sed ut perspiciatis unde omniste<br>natus error sit voluptatem acc.</p>
  <div class="card-stars">★★★★★</div>
  <div class="card-btn primary">ADD TO CART</div>
</article>

<article class="abs card" style="left:231px">
  <div class="card-photo" role="img" aria-label="Chocolate mousse in a glass beside chocolate pieces" style="background:linear-gradient(160deg,#d9cfc6,#8a5438 45%,#5a3322)"></div>
  <div class="card-price">$ 230.00</div>
  <p class="card-desc">Sed ut perspiciatis unde omniste<br>natus error sit voluptatem acc.</p>
  <div class="card-stars">★★★★★</div>
  <div class="card-btn">ADD TO CART</div>
</article>

<article class="abs card" style="left:365px">
  <div class="card-photo" role="img" aria-label="Brunavo dessert tub" style="background:linear-gradient(180deg,#4a4a48,#d9d2b6 45%,#c89a6a)"></div>
  <div class="card-price">$ 250.00</div>
  <p class="card-desc">Sed ut perspiciatis unde omniste<br>natus error sit voluptatem acc.</p>
  <div class="card-stars">★★★★★</div>
  <div class="card-btn">ADD TO CART</div>
</article>

<article class="abs card" style="left:500px">
  <div class="card-photo" role="img" aria-label="Vanilla ice cream scoops in a bowl with mint" style="background:linear-gradient(150deg,#cfe0c8,#f4f0e2 50%,#a8c8c0)"></div>
  <div class="card-price">$ 280.00</div>
  <p class="card-desc">Sed ut perspiciatis unde omniste<br>natus error sit voluptatem acc.</p>
  <div class="card-stars">★★★★★</div>
  <div class="card-btn">ADD TO CART</div>
</article>

<section class="abs quote">
  <h2 class="quote-title">"Raw, No added sugar, gluten-free"</h2>
  <p class="quote-text">Sed ut perspiciatis unde omnis iste natus error sit voluptatem accusantium doloremque laudantium, totam rem aperiam, eaque ipsa quae ab illo inventore veritatis et quasi architecto beatae vitae dicta sunt explicabo Nemo enim ipsam voluptateis et quasi architecto beam quia voluptas sit asperna</p>
</section>

<section class="abs newsletter">
  <div class="bowl" role="img" aria-label="Wooden bowl of fresh fruit, peppers and nuts"></div>
  <h2 class="news-title">Newsletter</h2>
  <p class="news-sub">Sign up for our mailing list to get latest updates and offers</p>
  <div class="news-form">
    <div class="news-field">Email Address:</div>
    <div class="news-btn">SIGNUP</div>
  </div>
</section>

<footer class="abs footer">
  <div class="foot-col" style="left:97px">
    <div class="foot-head">Contact</div>
    <div style="margin-top:21px">
      <div class="contact-row"><span class="contact-icon"><svg width="6" height="7" viewBox="0 0 6 7"><path d="M3 6.5C1 4 .8 3.2.8 2.6a2.2 2.2 0 0 1 4.4 0C5.2 3.2 5 4 3 6.5z" fill="none" stroke="#bbb" stroke-width=".7"/></svg></span><span>48 Alder Court, North 9th<br>Street, loremipsum.</span></div>
      <div class="contact-row"><span class="contact-icon"><svg width="6" height="6" viewBox="0 0 6 6"><path d="M1 .6l1.2 1.2-.6.9a3.5 3.5 0 0 0 1.7 1.7l.9-.6L5.4 5 4.6 5.6C2.6 5.4.6 3.4.4 1.4z" fill="none" stroke="#bbb" stroke-width=".6"/></svg></span><span>+0100 0200 30<br>+1555 01 2200</span></div>
      <div class="contact-row"><span class="contact-icon"><svg width="7" height="5" viewBox="0 0 7 5"><rect x=".4" y=".4" width="6.2" height="4.2" fill="none" stroke="#bbb" stroke-width=".6"/><path d="M.4.4l3.1 2.4L6.6.4" fill="none" stroke="#bbb" stroke-width=".6"/></svg></span><span>hello@varbek-mail.com</span></div>
    </div>
  </div>
  <div class="foot-col" style="left:232px">
    <div class="foot-head">Information</div>
    <ul class="foot-list"><li>About Us</li><li>Delivery Information</li><li>Privacy Policy</li><li>Terms &amp; Conditions</li><li>Blog</li><li>Careers</li></ul>
  </div>
  <div class="foot-col" style="left:353px">
    <div class="foot-head">Customer Service</div>
    <ul class="foot-list"><li>Contact Us</li><li>Returns</li><li>Site Map</li><li>Gift Certificates</li><li>Affiliates</li><li>Specials</li></ul>
  </div>
  <div class="foot-col" style="left:470px">
    <div class="foot-head">My Account</div>
    <ul class="foot-list"><li>My Account</li><li>Order History</li><li>Wish List</li><li>Newsletter</li><li>Our Products</li><li>Herbal</li></ul>
  </div>
  <div class="foot-col" style="left:576px">
    <div class="foot-head">Extras</div>
    <ul class="foot-list"><li>Gift Certificates</li><li>Affiliates</li><li>Specials</li><li>Wish List</li><li>My Account</li><li>Order History</li></ul>
  </div>
</footer>

<div class="abs foot-rule"></div>
<div class="abs foot-accent" style="left:97px"></div>
<div class="abs foot-accent" style="left:232px"></div>
<div class="abs foot-accent" style="left:353px"></div>
<div class="abs foot-accent" style="left:470px"></div>
<div class="abs foot-accent" style="left:576px"></div>

<div class="abs foot-bottom"></div>
<div class="abs social" style="left:89px;background:#3b5a9a"></div>
<div class="abs social" style="left:109px;background:#1fa6e0"></div>
<div class="abs social" style="left:129px;background:#50729a"></div>
<div class="abs social" style="left:148px;background:#dc4a38"></div>
<div class="abs social" style="left:168px;background:#c8202b"></div>
<div class="abs social" style="left:187px;background:#d42a22"></div>
<div class="abs copyright">Copyright © 2018 Varbek.All Rights reserved.</div>

</body>
</html>
```